'Ormel Property Development' Business Card

Business Card Features:

High Quality (potentially textured) thick card - preference is white textured card

Logo (supplied)

We plan to use the vertical logo as the main logo. But i am happy for people to use either if they find it works better for the design of the card.

The building icon and also the insert to the 'E' is in a metallic finish, i think this should be finished in a metallic embossed or raised style.
Updates

Please note i have attached both a horizontal and Vertical Logo for your reference. We plan to use the vertical logo as the main logo. But i am happy for people to use either if they find it works better for the design of the card.

Please note i am considering having the cards made on stainless steel. This introduces the option of having cut outs in the card and etching or printing for the design. If you have a good concept for this please submit.

http://www.tinquarry.example/black-metal-cards# this is a site that makes the metal cards to offer some direction . . . . Please note i am basic the selection o the best design, if that means normal print cards on paper then this is what i will choose. But there are some great options with the metal. Thanks.

Industry/Entity Type

Building

Requirements
Must have
• Helvetica font to details side of card - logo as supplied to opposite side.

Card Details:

Darrow Pketts
Managing Director

+61 487 263 518
+61 3 6172 4809

PO Box 73
Bentleigh, VIC 3024

darrow@ormel.example

www.ormel.example

```html
<!DOCTYPE html>
<html lang="en">
<head>
<meta charset="utf-8">
<title>Ormel Property Development – Business Card</title>
<link rel="stylesheet" href="https://fonts.googleapis.com/css2?family=Arimo:wght@400;700&display=swap">
<style>
  :root {
    --backdrop: #232325;
    --card-white: #ffffff;
    --card-grey: #e1e1e2;
    --band-light: #b8b8ba;
    --band-dark: #4c5053;
    --ink-dark: #4a4d50;
    --ink-mid: #7d8084;
    --ink-soft: #a6a8ab;
    --pattern-tone: #e4e4e5;
    --watermark: #d2d2d4;
  }
  * { margin: 0; padding: 0; box-sizing: border-box; }
  html, body { width: 1200px; height: 800px; overflow: hidden; }
  body {
    background: var(--backdrop);
    font-family: "Arimo", Helvetica, Arial, sans-serif;
    position: relative;
  }
  .card {
    position: absolute;
    top: 235px;
    width: 540px;
    height: 330px;
    overflow: hidden;
  }
  .card--front { left: 40px; background: var(--card-white); }
  .card--back { left: 620px; background: var(--card-grey); }
  .card__bands { position: absolute; inset: 0; }

  /* front: details side */
  .holder { position: absolute; left: 38px; top: 40px; }
  .holder__name { font-size: 17px; color: var(--ink-dark); letter-spacing: .3px; }
  .holder__role { font-size: 9px; color: var(--ink-soft); margin-top: 3px; }
  .contact-list { position: absolute; left: 34px; top: 92px; list-style: none; }
  .contact-list li {
    display: flex; align-items: center; gap: 10px;
    height: 21px; font-size: 10px; color: var(--ink-mid);
  }
  .contact-list svg { width: 12px; height: 12px; flex: none; }
  .square-field {
    position: absolute; left: 165px; top: 105px; width: 230px; height: 190px;
    background: radial-gradient(ellipse at 50% 50%, var(--pattern-tone), rgba(228,228,229,0) 72%);
  }
  .wordmark {
    position: absolute; left: 300px; top: 122px;
    font-weight: 700; font-size: 60px; letter-spacing: 2px; color: var(--ink-dark);
    display: flex; align-items: center; gap: 12px;
  }
  .wordmark__dot { width: 12px; height: 12px; background: var(--ink-soft); }
  .tagline {
    position: absolute; right: 24px; bottom: 16px;
    font-size: 11px; font-weight: 700; letter-spacing: 1.5px;
    text-transform: uppercase; color: var(--ink-mid);
  }

  /* back: logo side */
  .watermark {
    position: absolute; left: -10px; top: 60px;
    font-weight: 700; font-size: 190px; letter-spacing: 6px; color: var(--watermark);
    line-height: 1;
  }
  .back-mark { position: absolute; left: 0; right: 0; top: 118px; text-align: center; }
  .back-mark__name { font-weight: 700; font-size: 66px; letter-spacing: 3px; color: var(--ink-dark); line-height: 1; }
  .back-mark__tag {
    margin-top: 8px; font-size: 13px; font-weight: 700; letter-spacing: 2px;
    text-transform: uppercase; color: var(--ink-mid);
  }
</style>
</head>
<body>

<section class="card card--front" aria-label="Business card, details side">
  <svg class="card__bands" viewBox="0 0 540 330" aria-hidden="true">
    <polygon points="0,0 540,0 540,12 0,12" fill="var(--band-light)"/>
    <polygon points="300,12 540,12 540,24 320,24" fill="var(--band-dark)"/>
    <polygon points="0,316 540,316 540,330 0,330" fill="var(--band-dark)"/>
    <polygon points="0,306 250,306 262,316 0,316" fill="var(--band-light)"/>
    <polygon points="250,300 540,300 540,320 262,320" fill="var(--band-light)"/>
  </svg>

  <div class="square-field" role="img" aria-label="Field of soft grey squares behind the name"></div>

  <div class="holder">
    <p class="holder__name">Darrow Pketts</p>
    <p class="holder__role">Managing Director</p>
  </div>

  <ul class="contact-list">
    <li>
      <svg viewBox="0 0 12 12"><rect x="3" y="0.5" width="6" height="11" rx="1" fill="none" stroke="var(--ink-dark)"/><circle cx="6" cy="9.6" r=".7" fill="var(--ink-dark)"/></svg>
      +61 487 263 518
    </li>
    <li>
      <svg viewBox="0 0 12 12"><path d="M2.5 1 L4.5 1 L5.2 3.6 L4 4.6 Q5.2 7.2 7.4 8 L8.4 6.8 L11 7.5 L11 9.5 Q10.5 11 8.5 11 Q2 9.5 1 3 Q1 1.3 2.5 1Z" fill="var(--ink-dark)"/></svg>
      1800 318 742
    </li>
    <li>
      <svg viewBox="0 0 12 12"><circle cx="6" cy="6" r="5.5" fill="var(--ink-dark)"/><text x="6" y="8.6" font-size="7.5" text-anchor="middle" fill="#fff" font-family="Arimo, sans-serif">@</text></svg>
      darrow@ormel.example
    </li>
    <li>
      <svg viewBox="0 0 12 12"><path d="M6 11.5 Q2 7 2 4.5 A4 4 0 0 1 10 4.5 Q10 7 6 11.5Z" fill="none" stroke="var(--ink-dark)"/><circle cx="6" cy="4.5" r="1.4" fill="var(--ink-dark)"/></svg>
      www.ormel.example
    </li>
    <li>
      <svg viewBox="0 0 12 12"><rect x="0.5" y="2.5" width="11" height="7.5" fill="var(--ink-dark)"/><path d="M0.5 2.5 L6 7 L11.5 2.5" fill="none" stroke="#fff" stroke-width=".8"/></svg>
      PO BOX 73 BENTLEIGH VIC 3024
    </li>
  </ul>

  <div class="wordmark"><span>ORMEL</span><span class="wordmark__dot"></span></div>

  <p class="tagline">Property Development</p>
</section>

<section class="card card--back" aria-label="Business card, logo side">
  <svg class="card__bands" viewBox="0 0 540 330" aria-hidden="true">
    <polygon points="0,0 540,0 540,10 0,10" fill="var(--band-light)"/>
    <polygon points="330,10 540,10 540,22 350,22" fill="var(--band-dark)"/>
    <polygon points="0,314 540,314 540,330 0,330" fill="var(--band-light)"/>
  </svg>

  <div class="watermark" aria-hidden="true">ORMEL</div>

  <div class="back-mark">
    <p class="back-mark__name">ORMEL</p>
    <p class="back-mark__tag">Property Development</p>
  </div>
</section>

</body>
</html>
```